Brand New Church Business Card Design. Needs to appeal to high school students, professionals.

Business Card. Bold lines and colors. Simple font. This is a new church looking to attract new families who have moved to the area. Business professionals mostly. have a working logo. may need a little tweaking. Church is designed to do excellent ministries for students and children. Like business card design in box on pixel guild homepage. Want a front and back side. Prefer colors to match the logo. But will lean on designers preferences and wisdom. DO NOT WANT A CROSS OR RELIGIOUS SYMBOL on the card.

Target Market(s)

Families, Professionals, Students

Industry/Entity Type

High School

Contact Information for Business Card

SaltRock ChurchSaltRock.atForrest Coulter904-515-8349Forrest@PineHollow.ev

Font styles to use
Sans Serif

Colors
0255a3
ffffff

Requirements
Must have
• Bold colors. Very Masculine. Creative
Nice to have
• On inkmarket.pixelguild.ev homepage in the business card design box. the card with the black, blue and gray looks really sharp. matches our logos.
Should not have
• no crosses or religious symbols.

```html
<!DOCTYPE html>
<html lang="en">
<head>
<meta charset="utf-8">
<title>PineHollow Church – Business Card</title>
<link rel="stylesheet" href="https://fonts.googleapis.com/css2?family=Open+Sans:wght@400;700;800&display=swap">
<style>
  :root {
    --backdrop: #e4e4e4;
    --card-black: #050505;
    --card-sheen: #1c1c1c;
    --brand-blue: #0a6fd0;
    --brand-blue-deep: #0255a3;
    --ink-white: #ffffff;
  }
  * { box-sizing: border-box; margin: 0; padding: 0; }
  html, body {
    width: 1200px; height: 852px; overflow: hidden;
    background: var(--backdrop);
    font-family: "Open Sans", Arial, sans-serif;
  }
  .card {
    position: absolute;
    width: 540px; height: 310px;
    border-radius: 14px;
    overflow: hidden;
    background: linear-gradient(125deg, var(--card-black) 0%, var(--card-sheen) 45%, var(--card-black) 70%);
    box-shadow: 0 6px 14px rgba(0,0,0,.35);
  }
  .card--front { left: 150px; top: 110px; }
  .card--back  { left: 510px; top: 430px; }

  .front-mark {
    position: absolute; left: 50%; top: 50%;
    transform: translate(-50%, -50%);
    display: flex; align-items: center; gap: 14px;
  }
  .mark-dot {
    width: 56px; height: 56px; border-radius: 50%;
    background: var(--brand-blue);
  }
  .mark-name {
    color: var(--brand-blue);
    font-weight: 800; font-size: 30px; letter-spacing: -0.5px;
  }

  .holder-name {
    position: absolute; right: 22px; top: 28px;
    font-weight: 800; font-size: 19px;
  }
  .holder-name .first { color: var(--brand-blue); }
  .holder-name .last  { color: var(--ink-white); }

  .back-logo {
    position: absolute; left: 40px; top: 120px;
    display: flex; align-items: center; gap: 12px;
  }
  .back-logo .mark-dot { width: 62px; height: 62px; }
  .back-logo .mark-name { color: var(--ink-white); font-size: 30px; }

  .wave { position: absolute; inset: 0; }

  .contact {
    position: absolute; right: 16px; top: 168px;
    list-style: none;
    color: var(--ink-white);
    font-size: 14px; line-height: 25px;
    text-align: right;
  }
  .contact li { display: flex; align-items: center; justify-content: flex-end; gap: 10px; }
  .contact svg { width: 13px; height: 13px; fill: var(--ink-white); }
</style>
</head>
<body>

<section class="card card--front" aria-label="Card front">
  <div class="front-mark">
    <span class="mark-dot"></span>
    <span class="mark-name">PineHollow Church</span>
  </div>
</section>

<section class="card card--back" aria-label="Card back">
  <svg class="wave" viewBox="0 0 540 310" preserveAspectRatio="none" aria-hidden="true">
    <path d="M0,288 C150,258 250,262 320,190 C385,120 440,60 540,40 L540,310 L0,310 Z" fill="var(--brand-blue)"/>
    <path d="M0,284 C160,250 262,248 330,178 C392,112 450,62 540,46" fill="none" stroke="var(--card-black)" stroke-width="5"/>
    <path d="M0,296 C170,266 280,262 345,195 C400,140 460,90 540,64" fill="none" stroke="var(--card-black)" stroke-width="2.5"/>
    <path d="M0,270 C140,240 240,240 308,176 C370,116 430,58 540,30" fill="none" stroke="var(--brand-blue-deep)" stroke-width="3"/>
  </svg>

  <p class="holder-name"><span class="first">Dwayne</span> <span class="last">Mabry</span></p>

  <div class="back-logo">
    <span class="mark-dot"></span>
    <span class="mark-name">PineHollow Church</span>
  </div>

  <ul class="contact">
    <li>612-473-2096
      <svg viewBox="0 0 16 16" aria-hidden="true"><path d="M3 1h3l1.5 4-2 1.5a9 9 0 0 0 4 4L11 8.5l4 1.5v3a2 2 0 0 1-2 2A12 12 0 0 1 1 3a2 2 0 0 1 2-2z"/></svg>
    </li>
    <li>www.PineHollow.ev
      <svg viewBox="0 0 16 16" aria-hidden="true"><path d="M8 0a8 8 0 1 0 0 16A8 8 0 0 0 8 0zm0 1.5c.8 0 1.8 1.9 2.1 5.5H5.9C6.2 3.4 7.2 1.5 8 1.5zM1.6 9h2.8c.1 2 .5 3.7 1.1 4.9A6.5 6.5 0 0 1 1.6 9zm0-2a6.5 6.5 0 0 1 3.9-4.9C4.9 3.3 4.5 5 4.4 7zm6.4 7.5c-.8 0-1.8-1.9-2.1-5.5h4.2c-.3 3.6-1.3 5.5-2.1 5.5zm2.5-.6c.6-1.2 1-2.9 1.1-4.9h2.8a6.5 6.5 0 0 1-3.9 4.9zM11.6 7c-.1-2-.5-3.7-1.1-4.9A6.5 6.5 0 0 1 14.4 7z"/></svg>
    </li>
    <li>Dwayne@PineHollow.ev
      <svg viewBox="0 0 16 16" aria-hidden="true"><path d="M0 3h16v10H0zM1.5 4.5 8 9l6.5-4.5v-.2h-13z"/></svg>
    </li>
  </ul>
</section>

</body>
</html>
```